Vorla Advise Business Cards

We need a business card design for Vorla Advise (Logo Attached), a management consultancy specialized in brand & business building.

Design should be clean, smart and a touch of innnovation without being gimmicky.

The details on the card should be:
Name: Tomas Vellaquin
Title: Managing Director
Address: 42 Marden Wharf, Kestrel Tower Building, Singapore 073296
Tel: +6284729156048
email: tv@vorlaadvise.example
website: vorlaadvise.example

For further background on corporate identity, please check www.vorlaadvise.example
Updates

Dear all,

Many thanks for the submissions so far! I gave feedback to those designs that I prefer at this stage.

Overall I see that my preference goes into the direction that 'less is more' and 'simple is beautiful'

Please create uniqueness and standout by the simplicity and attraction of the overall concept and design.

Many thanks and please shout incase of questions!

Tomas

Industry/Entity Type

Business

```html
<!DOCTYPE html>
<html lang="en">
<head>
<meta charset="utf-8">
<title>Vorla Advise Business Cards</title>
<link rel="stylesheet" href="https://fonts.googleapis.com/css2?family=Open+Sans:wght@400;600;700&display=swap">
<style>
  :root {
    --bg: #e6e4e1;
    --card: #ffffff;
    --orange: #ee6a24;
    --rule: #1a1a1a;
    --ink: #4a4a4a;
  }
  * { box-sizing: border-box; margin: 0; padding: 0; }
  html, body { width: 1200px; height: 799px; overflow: hidden; }
  body {
    background: var(--bg);
    font-family: "Open Sans", Arial, sans-serif;
    position: relative;
  }
  .card {
    position: absolute;
    top: 251px;
    width: 520px;
    height: 297px;
    background: var(--card);
    box-shadow: 0 10px 24px rgba(0,0,0,0.14), 0 2px 4px rgba(0,0,0,0.08);
    overflow: hidden;
  }
  .card--front { left: 50px; }
  .card--back { left: 630px; }
  .card__band {
    position: absolute;
    left: 0; right: 0; bottom: 0;
    height: 64px;
    background: var(--orange);
    border-top: 5px solid var(--rule);
  }
  .company-name {
    color: var(--ink);
    font-weight: 600;
    white-space: nowrap;
  }
  .card--front .company-name {
    position: absolute;
    left: 0; right: 0;
    top: 88px;
    text-align: center;
    font-size: 42px;
  }
  .card--back .company-name {
    position: absolute;
    right: 26px;
    top: 26px;
    font-size: 22px;
  }
  .contact {
    position: absolute;
    left: 24px;
    top: 22px;
    list-style: none;
    max-width: 300px;
  }
  .contact__item {
    display: flex;
    align-items: center;
    gap: 7px;
    height: 15px;
    margin-bottom: 3px;
    font-size: 8.5px;
    color: var(--ink);
    white-space: nowrap;
  }
  .contact__icon {
    width: 12px; height: 12px;
    background: var(--orange);
    display: flex; align-items: center; justify-content: center;
    flex: none;
  }
  .contact__icon svg { width: 8px; height: 8px; }
  .person {
    position: absolute;
    right: 26px;
    bottom: 84px;
    text-align: right;
    color: var(--orange);
  }
  .person__name { font-size: 19px; font-weight: 700; line-height: 1.1; }
  .person__title { font-size: 10px; font-weight: 400; margin-top: 2px; }
</style>
</head>
<body>
  <section class="card card--front">
    <div class="company-name">Vorla Advise</div>
    <div class="card__band"></div>
  </section>

  <section class="card card--back">
    <ul class="contact">
      <li class="contact__item">
        <span class="contact__icon"><svg viewBox="0 0 8 8"><path d="M4 0.5a2.5 2.5 0 0 1 2.5 2.5c0 1.8-2.5 4.5-2.5 4.5S1.5 4.8 1.5 3A2.5 2.5 0 0 1 4 0.5z" fill="#fff"/><circle cx="4" cy="3" r="0.9" fill="#ee6a24"/></svg></span>
        42 Marden Wharf, Kestrel Tower Building, Singapore 073296
      </li>
      <li class="contact__item">
        <span class="contact__icon"><svg viewBox="0 0 8 8"><path d="M1.5 0.8l1.3-0.3 0.8 1.8-0.9 0.7c0.4 0.9 1.1 1.6 2 2l0.7-0.9 1.8 0.8-0.3 1.3C4 6.4 1.6 4 1.5 0.8z" fill="#fff"/></svg></span>
        +6284729156048
      </li>
      <li class="contact__item">
        <span class="contact__icon"><svg viewBox="0 0 8 8"><rect x="0.8" y="1.8" width="6.4" height="4.4" fill="#fff"/><path d="M0.8 1.8L4 4.4l3.2-2.6" fill="none" stroke="#ee6a24" stroke-width="0.7"/></svg></span>
        tv@vorlaadvise.example
      </li>
      <li class="contact__item">
        <span class="contact__icon"><svg viewBox="0 0 8 8"><circle cx="4" cy="4" r="3" fill="none" stroke="#fff" stroke-width="0.8"/><path d="M1 4h6M4 1c-1.4 1.7-1.4 4.3 0 6M4 1c1.4 1.7 1.4 4.3 0 6" fill="none" stroke="#fff" stroke-width="0.6"/></svg></span>
        vorlaadvise.example
      </li>
    </ul>
    <div class="company-name">Vorla Advise</div>
    <div class="person">
      <div class="person__name">Tomas Vellaquin</div>
      <div class="person__title">Managing Director</div>
    </div>
    <div class="card__band"></div>
  </section>
</body>
</html>
```